Stationery Design Project

We need letterhead and business cards designed for our consulting firm. Color scheme, mostly deep blue (see logo). We are a commercial consulting work out firm, nationwide (large loans, $10MM and up). Visit our website for more info.
Updates

Project Deadline Extended
Reason: Meeting tomorrow morning to make final final decision. Would like this project to stay open to be able to provide feed back and receive final edits and approve. Thank you!!!

Target Market(s)

High end investors

Industry/Entity Type

Business

Requirements
Must have
• Letterhead must have the logo and the address

4817 Larkmoor Avenue, Suite 210, San Diego, CA 92107
Nice to have
• It would be nice to incorporate a watermark of all or some portion of the logo on the letterhead, or at least for the 2nd sheets.

Maybe our phone number: 858.555.0174
and/or webiste: www.tollandridgecap.example
Should not have
• Target users and audience of this will be men so, frilly or whimsical type designs are not preferred.

```html
<!DOCTYPE html>
<html lang="en">
<head>
<meta charset="utf-8">
<title>Tolland Ridge Capital – Business Cards</title>
<link href="https://fonts.googleapis.com/css2?family=Arimo:wght@400;700&display=swap" rel="stylesheet">
<style>
  :root {
    --stage: #959fa6;
    --label: #f4f6f7;
    --sky: #5bbff7;
    --paper: #ffffff;
    --ink: #4a4d50;
    --brand-grey: #5f676c;
    --name-blue: #1f78d6;
    --accent-blue: #5aaae8;
    --rule-blue: #8cc6ee;
    --shadow: rgba(0, 0, 0, 0.55);
  }
  * { box-sizing: border-box; margin: 0; padding: 0; }
  html, body { width: 1200px; height: 900px; overflow: hidden; }
  body {
    background: var(--stage);
    font-family: "Arimo", Arial, sans-serif;
    position: relative;
    color: var(--ink);
  }
  .view-label {
    position: absolute;
    color: var(--label);
    font-size: 20px;
    letter-spacing: 1.5px;
  }
  .card {
    position: absolute;
    width: 545px;
    height: 332px;
    border-radius: 24px;
    background: var(--paper);
    box-shadow: 6px 7px 5px var(--shadow);
    overflow: hidden;
  }
  .card--front { left: 328px; top: 88px; background: var(--sky); }
  .card--back-one { left: 36px; top: 480px; }
  .card--back-two { left: 618px; top: 480px; }

  .brand {
    position: absolute;
    display: flex;
    flex-direction: column;
    align-items: center;
    color: var(--brand-grey);
    font-weight: 700;
    white-space: nowrap;
  }
  .brand__mark { background: var(--brand-grey); }
  .card--front .brand { left: 0; right: 0; top: 98px; gap: 18px; font-size: 36px; }
  .card--front .brand__mark { width: 62px; height: 62px; }
  .card--back-one .brand { left: 20px; width: 190px; top: 133px; gap: 9px; font-size: 17px; }
  .card--back-one .brand__mark { width: 30px; height: 30px; }
  .card--back-two .brand { left: 14px; width: 228px; top: 84px; gap: 12px; font-size: 21px; }
  .card--back-two .brand__mark { width: 36px; height: 36px; }

  .divider {
    position: absolute;
    width: 2px;
    background: var(--rule-blue);
  }
  .card--back-one .divider { left: 224px; top: 60px; height: 215px; }
  .card--back-two .divider { left: 249px; top: 80px; height: 167px; }

  .details {
    position: absolute;
    font-size: 16px;
    line-height: 20.6px;
    white-space: nowrap;
  }
  .card--back-one .details { left: 257px; top: 59px; }
  .card--back-two .details { left: 268px; top: 82px; }
  .person__name { color: var(--name-blue); font-size: 18px; font-weight: 700; line-height: 22px; }
  .person__title { margin-bottom: 13px; }
  .address { margin-bottom: 14px; }
  .contact__label { color: var(--accent-blue); }
  .contact__web { color: var(--accent-blue); }

  .card--back-two .address {
    position: absolute;
    left: 10px;
    width: 228px;
    top: 209px;
    text-align: center;
    font-size: 14.5px;
    line-height: 21px;
    white-space: nowrap;
    margin: 0;
  }
  .card--back-two .person__title { margin-bottom: 23px; }
</style>
</head>
<body>
  <div class="view-label" style="left:328px; top:46px;">front</div>
  <section class="card card--front">
    <div class="brand"><span class="brand__mark"></span><span class="brand__name">Tolland Ridge Capital</span></div>
  </section>

  <section class="card card--back-one">
    <div class="brand"><span class="brand__mark"></span><span class="brand__name">Tolland Ridge Capital</span></div>
    <div class="divider"></div>
    <div class="details">
      <div class="person__name">Evan Marlow</div>
      <div class="person__title">Chief Executive Officer</div>
      <div class="address">4817 Larkmoor Avenue, Suite 210<br>San Diego, CA 92107</div>
      <div class="contact">
        <div><span class="contact__label">tel:</span>&nbsp; 858 555 0174</div>
        <div><span class="contact__label">fax:</span> 858 555 0189</div>
        <div><span class="contact__label">cell:</span> 858 555 0123</div>
        <div><span class="contact__label">e-mail:</span> info@tollandridgecap.example</div>
        <div class="contact__web">www.tollandridgecap.example</div>
      </div>
    </div>
  </section>
  <div class="view-label" style="left:36px; top:833px;">back 1st option</div>

  <section class="card card--back-two">
    <div class="brand"><span class="brand__mark"></span><span class="brand__name">Tolland Ridge Capital</span></div>
    <div class="address">4817 Larkmoor Avenue, Suite 210<br>San Diego, CA 92107</div>
    <div class="divider"></div>
    <div class="details">
      <div class="person__name">Evan Marlow</div>
      <div class="person__title">Chief Executive Officer</div>
      <div class="contact">
        <div><span class="contact__label">tel:</span>&nbsp; 858 555 0174</div>
        <div><span class="contact__label">fax:</span> 858 555 0189</div>
        <div><span class="contact__label">cell:</span> 858 555 0123</div>
        <div><span class="contact__label">e-mail:</span> info@tollandridgecap.example</div>
        <div class="contact__web">www.tollandridgecap.example</div>
      </div>
    </div>
  </section>
  <div class="view-label" style="left:618px; top:833px;">back 2nd option</div>
</body>
</html>
```